Roadwise Beacon Traffic Control Company Website

Modern website Wordpress design using all greyscale photos with a pop of red (such as road closure signs or detour cones) for strategic emphasis. (see brand guide for color codes)
The creative goal is to leverage high-contrast, desaturated imagery to create a clean, professional, and industrial feel. The selective use of red will draw immediate attention to critical elements—such as road hazards, safety equipment, or key messages to ensure the viewer's focus is directed with purpose.

Brand guide, homepage content and logo are attached. Create clean professional user experience to market services to industry professionals.

```html
<!DOCTYPE html>
<html lang="en">
<head>
<meta charset="utf-8">
<title>Roadwise Beacon Traffic Control Company</title>
<link href="https://fonts.googleapis.com/css2?family=Rubik:wght@600;700;800&family=Inter:wght@400;500;600&display=swap" rel="stylesheet">
<style>
:root{
  --red:#e51b23;
  --ink:#111111;
  --text:#1c1c1c;
  --muted:#5a5a5a;
  --light:#efefef;
  --white:#ffffff;
  --line:#d8d8d8;
  --footer:#1b1b1b;
  --placeholder:#7c7c7c;
}
*{box-sizing:border-box;margin:0;padding:0}
html,body{width:1200px;height:2542px;overflow:hidden}
body{font-family:"Inter",sans-serif;color:var(--text);background:var(--white);position:relative}
.abs{position:absolute}
.heading{font-family:"Rubik",sans-serif;font-weight:700}
.btn{position:absolute;display:flex;align-items:center;justify-content:center;border-radius:6px;font-size:15px;font-weight:600;text-transform:uppercase}
.btn-red{background:var(--red);color:var(--white)}
.btn-ghost{border:1px solid var(--white);color:var(--white)}
.brand{font-family:"Inter",sans-serif;font-weight:600;color:var(--white);display:flex;align-items:center;gap:8px}
.brand i{display:block;width:14px;height:14px;background:var(--red)}

/* hero */
.hero{top:0;left:0;width:1200px;height:676px;background:radial-gradient(circle at 78% 33%,#8a2a30 0,#4a3536 18%,rgba(40,40,40,0) 32%),linear-gradient(90deg,#3a3a3a 0%,#555 40%,#2f2f2f 100%)}
.hero-shade{top:0;left:0;width:1200px;height:676px;background:linear-gradient(90deg,rgba(0,0,0,.45),rgba(0,0,0,.1))}
.nav a{position:absolute;top:38px;font-size:14px;color:var(--white);text-decoration:none}
.nav .active{color:var(--red)}
.hero-title{left:62px;top:212px;font-size:52px;line-height:63px;color:var(--white)}
.hero-title span{color:var(--red)}
.hero-sub{left:62px;top:414px;font-size:16px;color:var(--white)}

/* services */
.services{top:676px;left:0;width:1200px;height:550px;background:var(--light)}
.services-title{top:68px;width:1200px;text-align:center;font-size:34px;font-weight:800;color:var(--ink)}
.services-title span{color:var(--red)}
.card{position:absolute;width:256px;height:165px;background:var(--white);border-radius:10px;border-left:3px solid var(--red);padding:28px 6px 0 21px}
.card-head{display:flex;align-items:center;gap:14px;height:44px}
.card-icon{flex:none;width:42px;height:42px;border-radius:50%;background:#f1f1f1;display:flex;align-items:center;justify-content:center}
.card h3{font-size:14.5px;font-weight:600;line-height:21px;color:var(--ink);letter-spacing:-.1px}
.card p{margin-top:18px;font-size:12.6px;line-height:18px;color:var(--muted);letter-spacing:-.15px}

/* about */
.about-title{left:62px;top:1312px;font-size:32px;line-height:41px;color:var(--ink)}
.about-title span{color:var(--red)}
.industries{left:62px;top:1455px;font-size:15px;font-weight:600}
.checks{left:62px;top:1490px;list-style:none;font-size:13.5px;color:var(--muted)}
.checks li{display:flex;align-items:center;gap:9px;height:26px}
.photo-frame{left:619px;top:1305px;width:508px;height:343px;border:1.5px solid var(--red)}
.photo{left:628px;top:1314px;width:512px;height:340px;background:linear-gradient(120deg,#9a9a9a,#d9d9d9 55%,#7d7d7d)}
.badge{left:1028px;top:1585px;width:108px;height:66px;background:var(--white)}

/* features */
.features{left:60px;top:1730px;width:1080px;height:98px;border-top:1px solid var(--line);border-bottom:1px solid var(--line)}
.feature{position:absolute;top:22px;display:flex;align-items:center;gap:14px;font-size:17px;font-weight:500;line-height:24px;color:var(--ink)}
.partner{left:530px;top:1855px;width:134px;height:44px;border-radius:6px;background:#1f3c74}

/* cta */
.cta{top:1952px;left:0;width:1200px;height:290px;background:linear-gradient(90deg,#5a5a5a,#6e6e6e 50%,#555)}
.cta-side{width:100px;background:var(--placeholder)}
.cta-title{top:2030px;width:1200px;text-align:center;font-size:30px;color:var(--white)}
.cta-sub{top:2078px;width:1200px;text-align:center;font-size:14.5px;color:var(--white)}

/* footer */
.footer{top:2242px;left:0;width:1200px;height:300px;background:var(--footer);color:#c9c9c9}
.footer h4{position:absolute;top:55px;font-family:"Rubik",sans-serif;font-size:18px;font-weight:600;color:var(--white)}
.footer ul{position:absolute;top:85px;list-style:none;font-size:13.5px;line-height:24px}
.footer-about{left:61px;top:133px;width:240px;font-size:13.5px;line-height:21px}
.social{position:absolute;top:207px;width:14px;height:14px;border-radius:50%;border:1.5px solid #c9c9c9}
.contact li{display:flex;align-items:center;gap:10px;height:30px}
.stripe{left:57px;top:2486px;width:1088px;height:6px;background:var(--red)}
.copy{top:2509px;width:1200px;text-align:center;font-size:12px;color:#d8d8d8}
</style>
</head>
<body>

<!-- hero -->
<div class="abs hero" role="img" aria-label="Greyscale photo of a flagger in a hard hat and vest holding a red stop paddle"></div>
<div class="abs hero-shade"></div>
<div class="abs brand" style="left:60px;top:30px;font-size:17px"><i></i>Roadwise Beacon</div>
<nav class="nav">
  <a class="active" style="left:435px">HOME</a>
  <a style="left:517px">ABOUT</a>
  <a style="left:609px">SERVICES</a>
  <a style="left:722px">RENTALS</a>
  <a style="left:827px">JOBS</a>
  <a style="left:900px">CONTACT</a>
</nav>
<div class="btn btn-red" style="left:994px;top:25px;width:146px;height:41px;font-size:15px">Get a Quote</div>
<h1 class="abs heading hero-title">Traffic Control<br>Solutions Engineered<br><span>For Safety.</span></h1>
<p class="abs hero-sub">Safety Isn’t A Priority, It’s The Foundation Of Everything We Do</p>
<div class="btn btn-red" style="left:60px;top:455px;width:146px;height:41px">Our Service</div>
<div class="btn btn-ghost" style="left:222px;top:454px;width:148px;height:42px">Get a Quote</div>

<!-- services -->
<section class="abs services">
  <h2 class="abs heading services-title"><span>OUR</span> SERVICES</h2>
  <div class="card" style="left:59px;top:127px"><div class="card-head"><div class="card-icon"><svg width="22" height="22" viewBox="0 0 22 22" fill="none" stroke="#e51b23" stroke-width="1.4"><circle cx="8" cy="5" r="2.5"/><path d="M8 8v12M5 11h6M14 3v17M14 4h5v4h-5"/></svg></div><h3>Flagging &amp; Lane<br>Closures</h3></div><p>Professional flaggers and lane closure services for construction zones and traffic redirection.</p></div>
  <div class="card" style="left:335px;top:127px"><div class="card-head"><div class="card-icon"><svg width="22" height="22" viewBox="0 0 22 22" fill="none" stroke="#e51b23" stroke-width="1.4"><rect x="2" y="5" width="18" height="7"/><path d="M5 12v8M17 12v8M6 5l4 7M12 5l4 7"/></svg></div><h3>Temporary Traffic<br>Control Plans</h3></div><p>Customized traffic control plans designed to ensure safety and compliance with regulatory standards.</p></div>
  <div class="card" style="left:611px;top:127px"><div class="card-head"><div class="card-icon"><svg width="22" height="22" viewBox="0 0 22 22" fill="none" stroke="#e51b23" stroke-width="1.4"><rect x="2" y="4" width="18" height="8"/><path d="M5 12v8M17 12v8M2 16h18"/></svg></div><h3>Signage &amp; Barricades</h3></div><p>Comprehensive signage and barricade solutions for all traffic control needs.</p></div>
  <div class="card" style="left:887px;top:127px"><div class="card-head"><div class="card-icon"><svg width="22" height="22" viewBox="0 0 22 22" fill="none" stroke="#e51b23" stroke-width="1.4"><rect x="1" y="6" width="13" height="9"/><path d="M14 9h4l3 3v3h-7"/><circle cx="5" cy="17" r="2"/><circle cx="17" cy="17" r="2"/></svg></div><h3>Crash &amp; Truck Mounted<br>Attenuators</h3></div><p>Mobile and fixed crash attenuation systems to protect work zones and minimize accident severity.</p></div>
  <div class="card" style="left:59px;top:311px"><div class="card-head"><div class="card-icon"><svg width="22" height="22" viewBox="0 0 22 22" fill="none" stroke="#e51b23" stroke-width="1.4"><path d="M3 14l2-6h12l2 6v4H3z"/><circle cx="7" cy="15" r="1"/><circle cx="15" cy="15" r="1"/></svg></div><h3>Heavy Highway Traffic<br>Control</h3></div><p>Specialized traffic management solutions for major highway projects and high-volume roadways.</p></div>
  <div class="card" style="left:335px;top:311px"><div class="card-head"><div class="card-icon"><svg width="22" height="22" viewBox="0 0 22 22" fill="none" stroke="#e51b23" stroke-width="1.4"><path d="M11 2v18M11 8l-6-4M11 8l6-4M5 4v3M17 4v3M7 14h8"/></svg></div><h3>Roadway Detours &amp;<br>Lane Shifts</h3></div><p>Strategic planning and implementation of detours and lane shifts for road construction projects.</p></div>
  <div class="card" style="left:611px;top:311px"><div class="card-head"><div class="card-icon"><svg width="22" height="22" viewBox="0 0 22 22" fill="none" stroke="#e51b23" stroke-width="1.4"><path d="M9 3h4l5 15H4z"/><path d="M3 19h16M7 10h8M6 14h10"/></svg></div><h3>Work Zone Safety<br>Consulting</h3></div><p>Expert consulting for compliance with TxDOT and OSHA regulations in work zone safety.</p></div>
  <div class="card" style="left:887px;top:311px"><div class="card-head"><div class="card-icon"><svg width="22" height="22" viewBox="0 0 22 22" fill="none" stroke="#e51b23" stroke-width="1.4"><path d="M3 9h16v10H3zM6 9v10M10 9v10M14 9v10M18 9v10"/><circle cx="7" cy="5" r="1.5"/><circle cx="15" cy="5" r="1.5"/></svg></div><h3>Event Traffic &amp; Crowd<br>Control</h3></div><p>Comprehensive traffic and crowd management for public and private events of all sizes.</p></div>
</section>

<!-- about -->
<h2 class="abs heading about-title">Serving Texas Industry to<br>Ensure <span>Safety</span>, Compliance,<br>and Efficient Traffic Flow</h2>
<p class="abs industries">Industries We Serve</p>
<ul class="abs checks">
  <li><svg width="13" height="13" viewBox="0 0 13 13"><circle cx="6.5" cy="6.5" r="6.5" fill="#e51b23"/><path d="M3.5 6.8l2 2 4-4" stroke="#fff" stroke-width="1.5" fill="none"/></svg>Road construction, maintenance, &amp; Detours</li>
  <li><svg width="13" height="13" viewBox="0 0 13 13"><circle cx="6.5" cy="6.5" r="6.5" fill="#e51b23"/><path d="M3.5 6.8l2 2 4-4" stroke="#fff" stroke-width="1.5" fill="none"/></svg>Municipal &amp; State projects</li>
  <li><svg width="13" height="13" viewBox="0 0 13 13"><circle cx="6.5" cy="6.5" r="6.5" fill="#e51b23"/><path d="M3.5 6.8l2 2 4-4" stroke="#fff" stroke-width="1.5" fill="none"/></svg>Private Sector &amp; Commercial Contractors</li>
  <li><svg width="13" height="13" viewBox="0 0 13 13"><circle cx="6.5" cy="6.5" r="6.5" fill="#e51b23"/><path d="M3.5 6.8l2 2 4-4" stroke="#fff" stroke-width="1.5" fill="none"/></svg>Oil, Gas, Wind, Solar, &amp; Manufacturing</li>
</ul>
<div class="btn btn-red" style="left:60px;top:1609px;width:146px;height:41px">Contact</div>
<div class="abs photo-frame"></div>
<div class="abs photo" role="img" aria-label="Greyscale photo of a flagger in a safety vest holding a red stop sign beside a road"></div>
<div class="abs badge" role="img" aria-label="Partner event badge"></div>

<!-- features -->
<div class="abs features">
  <div class="feature" style="left:28px"><svg width="44" height="50" viewBox="0 0 44 50" fill="none" stroke="#e51b23" stroke-width="1.6"><circle cx="22" cy="20" r="15"/><circle cx="22" cy="20" r="9"/><path d="M18 20l3 3 5-6M12 32l-5 14 7-3 4 6 3-10M32 32l5 14-7-3-4 6-3-10"/></svg><span>TxDOT-Compliant<br>&amp; Certified</span></div>
  <div class="feature" style="left:309px"><svg width="48" height="50" viewBox="0 0 48 50" fill="none" stroke="#e51b23" stroke-width="1.6"><circle cx="18" cy="20" r="6"/><path d="M6 46V36a12 12 0 0 1 20 -6M26 46h18V34h-8l-3-8-3 8h-4z"/><path d="M8 6l1.5 3 3 .4-2.2 2 .6 3-2.9-1.5L5 14.4l.6-3-2.2-2 3-.4zM24 2l1.5 3 3 .4-2.2 2 .6 3L24 9l-2.9 1.4.6-3-2.2-2 3-.4zM40 6l1.5 3 3 .4-2.2 2 .6 3-2.9-1.5-2.9 1.5.6-3-2.2-2 3-.4z"/></svg><span>Experienced &amp;<br>Trained Crew</span></div>
  <div class="feature" style="left:598px"><svg width="42" height="50" viewBox="0 0 42 50" fill="none" stroke="#e51b23" stroke-width="1.6"><path d="M21 2l18 7v14c0 12-8 20-18 25C11 43 3 35 3 23V9z"/><path d="M21 8l12 5v10c0 9-5 15-12 19-7-4-12-10-12-19V13z"/><path d="M15 24l5 5 8-9"/></svg><span>Reliable &amp;<br>Responsive</span></div>
  <div class="feature" style="left:840px"><svg width="50" height="50" viewBox="0 0 50 50" fill="none" stroke="#e51b23" stroke-width="1.6"><path d="M4 30h10v18H4zM14 34h10v14H14z"/><circle cx="34" cy="34" r="12"/><path d="M34 27v14M30 30h6a2 2 0 0 1 0 4h-4a2 2 0 0 0 0 4h6"/><path d="M20 18l8-14 8 14M28 4v18"/></svg><span>Cost-Effective &amp;<br>Efficient</span></div>
</div>
<div class="abs partner" role="img" aria-label="Industry association membership badge"></div>

<!-- cta -->
<section class="abs cta" role="img" aria-label="Greyscale road scene background"></section>
<div class="abs cta-side" style="left:60px;top:1975px;height:267px" role="img" aria-label="Photo of an orange traffic cone"></div>
<div class="abs cta-side" style="left:1022px;top:1965px;height:277px" role="img" aria-label="Photo of an orange traffic cone"></div>
<h2 class="abs heading cta-title">Need Professional Traffic Control Solutions?</h2>
<p class="abs cta-sub">Our team of certified experts is ready to help ensure safety and compliance on your next project.</p>
<div class="btn btn-red" style="left:428px;top:2124px;width:187px;height:42px">Get a Free Quote</div>
<div class="btn btn-ghost" style="left:624px;top:2124px;width:148px;height:43px">Contact Us</div>

<!-- footer -->
<footer class="abs footer">
  <div class="abs brand" style="left:61px;top:78px;font-size:15px"><i></i>Roadwise Beacon</div>
  <p class="abs footer-about">Professional traffic control solutions engineered for safety and compliance across Texas.</p>
  <span class="social" style="left:61px"></span>
  <span class="social" style="left:88px"></span>
  <span class="social" style="left:118px"></span>
  <h4 style="left:338px">Our Services</h4>
  <ul style="left:338px"><li>Flagging &amp; Lane Closures</li><li>Traffic Control Plans</li><li>Signage &amp; Barricades</li><li>Work Zone Safety Consulting</li></ul>
  <h4 style="left:614px">Quick Links</h4>
  <ul style="left:614px"><li>About Us</li><li>Services</li><li>Rentals</li><li>Careers</li><li>Contact Us</li></ul>
  <h4 style="left:889px">Contact Us</h4>
  <ul class="contact" style="left:889px;top:80px">
    <li><svg width="14" height="14" viewBox="0 0 14 14" fill="none" stroke="#c9c9c9" stroke-width="1.2"><path d="M7 13s5-5 5-8A5 5 0 0 0 2 5c0 3 5 8 5 8z"/><circle cx="7" cy="5" r="1.6"/></svg>450 Beacon Lane, Austin, TX 78702</li>
    <li><svg width="14" height="14" viewBox="0 0 14 14" fill="none" stroke="#c9c9c9" stroke-width="1.2"><path d="M3 1h2.5l1 3-1.5 1a7 7 0 0 0 4 4l1-1.5 3 1V11a2 2 0 0 1-2 2A11 11 0 0 1 1 3a2 2 0 0 1 2-2z"/></svg>(512) 555-0148</li>
    <li><svg width="14" height="14" viewBox="0 0 14 14" fill="none" stroke="#c9c9c9" stroke-width="1.2"><rect x="1" y="3" width="12" height="8"/><path d="M1 3l6 5 6-5"/></svg>info@roadwisebeacon.com</li>
  </ul>
</footer>
<div class="abs stripe"></div>
<p class="abs copy">©2025 ROADWISE BEACON- All rights reserved.</p>

</body>
</html>
```